Brochure Design for B-to-B software company

This project is for a product brochure in an 11x17 bifold format. The brochure will be a printed on heavy stock that will fold into 4 - 8 ½” x 11” pages. The folded edge will be on the left side. The brochure will be a combination of text and graphics. The completed editable files will be provided to us for further edits when needed. The color palette should complement and not overuse our logo colors.

Target Market(s)

Corporate Brands

Font styles to use
Sans Serif

Colors
cadf82

Requirements
Must have
• Color palette described in attached project overview document

```html
<!DOCTYPE html>
<html lang="en">
<head>
<meta charset="utf-8">
<title>Sales Platform Brochure Spread</title>
<link rel="stylesheet" href="https://fonts.googleapis.com/css2?family=Quicksand:wght@400;500;600;700&family=Open+Sans:wght@400;600&display=swap">
<style>
:root{
  --green:#8cc63f;
  --green-soft:#cadf82;
  --ink:#2e3236;
  --body:#4a4f54;
  --bar:#6b7178;
  --panel:#eef1f0;
  --line:#d9dcdf;
  --blue:#1e90d6;
  --paper:#ffffff;
}
*{margin:0;padding:0;box-sizing:border-box}
html,body{width:1200px;height:776px;overflow:hidden;background:var(--paper)}
.spread{position:relative;width:1200px;height:776px;font-family:"Quicksand",sans-serif;color:var(--body);overflow:hidden}
.leaf-wash{position:absolute;left:330px;top:-40px;width:560px;height:860px;border-radius:50%;
  background:radial-gradient(ellipse at center,rgba(202,223,130,.22) 0%,rgba(202,223,130,.10) 45%,rgba(255,255,255,0) 70%)}
.block{position:absolute}
h2{font-weight:600;color:var(--green);font-size:15.5px;line-height:18px}
h3{font-weight:500;color:var(--ink);font-size:12.4px;line-height:14.2px}
p{font-size:12px;line-height:14.2px;color:var(--body)}

/* screens */
.screen{position:absolute;background:#fff;font-family:"Open Sans",sans-serif;color:#666;font-size:3.6px;overflow:hidden}
.screen .abs{position:absolute}
.thead{background:var(--bar);color:#fff;font-weight:600}
.field{position:absolute;height:6px;border:.5px solid #c8cbce;background:#fff;font-size:3.2px;line-height:5px;padding-left:1px;color:#333}
.lbl{position:absolute;font-size:3px;color:#888;text-align:right}
.btn{position:absolute;background:var(--blue);color:#fff;font-size:3.6px;text-align:center}
.photo{position:absolute;background:linear-gradient(135deg,#7fa86a,#c9dcb4)}
.row{position:absolute;left:0;right:0;border-bottom:.5px solid #eee;font-size:3.4px}
.row span,.thead span{position:absolute}
</style>
</head>
<body>
<div class="spread">
  <div class="leaf-wash" role="img" aria-label="Faint large green leaf decoration behind the spread"></div>

  <!-- Left page -->
  <div class="block" style="left:34px;top:31px;width:535px">
    <h2>Branded Sales and CRM Portal</h2>
    <p style="margin-top:3px">Quickly launch a branded sales and CRM portal to manage your B-to-B sales channel. You set up your retailers in the portal including their locations and license information. Once set up, purchasers can sign-in and place orders. They can also access sales materials, product descriptions, videos and CoAs and other assets that you make available. Your sales team has access to all orders and can enter new orders quickly, as well.</p>
    <h2 style="margin-top:16px">Manage Orders Though Fulfillment</h2>
    <p style="margin-top:3px">Manage ordering processes with efficient easy-to-use tools for retailers and for your fulfillment and sales management teams</p>
  </div>

  <div class="block" style="left:34px;top:199px;width:218px">
    <h3>Enter Orders</h3>
    <p style="margin-top:4px">Retailers and your sales personnel easily enter orders, directing delivery to any of the customer’s locations. The order entry workflow is configured to meet your needs and terminology.</p>
    <h3 style="margin-top:18px">Manage Order Flow</h3>
    <p style="margin-top:4px">Retailers and your sales team track orders from start to finish. Workflow and automated notifications keep the retailer up-to-date on order progress. One button-click generates the invoice. Your workflow alerts if an order stagnates.</p>
  </div>

  <div class="block" style="left:34px;top:432px;width:535px">
    <h3>Support Your Fulfillment Process</h3>
    <p style="margin-top:4px">Provide your team with the tools they need for efficient and timely fulfillment/delivery. Receive automated notifications when an order is complete.</p>
    <h3 style="margin-top:14px">Manage Your Products, Discounts and Inventory</h3>
  </div>
  <div class="block" style="left:34px;top:510px;width:535px">
    <p>Set up product SKUs/codes with descriptions, prices and images. Using the inventory manage-</p>
    <p style="width:205px">ment feature you can also manage and track inventory. If you want to push a product you can configure special promotions and scheduled discounts in the product dashboard.</p>
  </div>
  <div class="block" style="left:34px;top:608px;width:215px">
    <h2>Pipeline and Sales Analytics</h2>
    <p style="margin-top:3px">Performance metrics calculated for all orders provide valuable real-time business intelligence. The sales pipeline dashboard shows weighted pipeline for all orders. Real-time key performance indicators (KPIs) are calculated for all retailers providing actionable information.</p>
  </div>

  <!-- Product screen -->
  <div class="screen" style="left:262px;top:202px;width:308px;height:206px">
    <div class="abs thead" style="left:0;top:0;width:308px;height:10px">
      <span style="left:37px;top:1px">Product Code/SKU</span><span style="left:65px;top:1px">Product Family</span><span style="left:117px;top:1px">Start Date</span><span style="left:136px;top:1px">End Date</span><span style="left:153px;top:1px">Unit Price</span><span style="left:169px;top:1px">Discount Price</span><span style="left:193px;top:1px">Discount Start</span><span style="left:222px;top:1px">Discount End</span><span style="left:249px;top:1px">Product URL</span>
    </div>
    <div class="abs" style="left:0;top:10px;width:308px;height:11px;background:#f4f4f4;font-size:3.2px;padding:2px 0">
      <span class="abs" style="left:0">Gumdrop - 10 mg - 20</span><span class="abs" style="left:37px">9001234</span><span class="abs" style="left:65px">CBD Infused Edibles</span><span class="abs" style="left:117px">06/1/19</span><span class="abs" style="left:136px">01/01/99</span><span class="abs" style="left:153px">$10.00</span><span class="abs" style="left:169px">$5.00</span><span class="abs" style="left:193px">03/01/19</span><span class="abs" style="left:222px">03/22/22</span><span class="abs" style="left:249px;color:var(--blue);text-decoration:underline">http://linkhub.com</span>
    </div>
    <div class="abs" style="left:11px;top:37px;font-size:4px">Product Details</div>
    <div class="abs" style="left:154px;top:36px;font-size:4px">Product Pricing</div>
    <div class="lbl" style="left:20px;top:45px;width:42px">Product Name:</div><div class="field" style="left:63px;top:44px;width:68px">Gumdrop CBD - 10 mg</div>
    <div class="lbl" style="left:20px;top:53px;width:42px">Product Description:</div><div class="field" style="left:63px;top:52px;width:68px;height:9px">CBD Infused Gumdrop - 10 mg - 20 pack</div>
    <div class="lbl" style="left:20px;top:69px;width:42px">Product Page URL:</div><div class="field" style="left:63px;top:68px;width:68px">https://fernway.com/gumdrops</div>
    <div class="lbl" style="left:20px;top:78px;width:42px">Product Family:</div><div class="field" style="left:63px;top:77px;width:63px">CBD Infused Edibles</div>
    <div class="lbl" style="left:20px;top:87px;width:42px">Product Code/SKU:</div><div class="field" style="left:63px;top:86px;width:78px">9001234</div>
    <div class="lbl" style="left:20px;top:95px;width:42px">Entry Product ID:</div><div class="field" style="left:63px;top:94px;width:78px">1234</div>
    <div class="lbl" style="left:20px;top:103px;width:42px">Product ID:</div><div class="field" style="left:63px;top:102px;width:78px">5678</div>
    <div class="lbl" style="left:155px;top:45px;width:47px">Unit Price:</div><div class="field" style="left:205px;top:44px;width:37px">$10.00</div>
    <div class="lbl" style="left:155px;top:53px;width:47px">Discount Price:</div><div class="field" style="left:205px;top:52px;width:37px">$5.00</div>
    <div class="lbl" style="left:155px;top:62px;width:47px">Discount Start Date:</div><div class="field" style="left:205px;top:61px;width:21px">3/1/2019</div>
    <div class="lbl" style="left:155px;top:71px;width:47px">Discount End Date:</div><div class="field" style="left:205px;top:70px;width:21px">3/22/2022</div>
    <div class="lbl" style="left:155px;top:80px;width:47px">Product Start Date:</div><div class="field" style="left:205px;top:79px;width:21px">6/11/2019</div>
    <div class="lbl" style="left:155px;top:88px;width:47px">Product End Date:</div><div class="field" style="left:205px;top:87px;width:21px">1/1/2099</div>
    <div class="lbl" style="left:155px;top:97px;width:47px">Reference Quantity:</div><div class="field" style="left:205px;top:96px;width:37px">20</div>
    <div class="abs" style="left:0;top:118px;width:308px;height:28px;background:var(--panel);text-align:center;font-size:3.8px;padding-top:3px;line-height:10px">Upload Files<br>Drag and Drop Files Here</div>
    <div class="abs thead" style="left:0;top:151px;width:308px;height:7px;font-size:3.4px"><span style="left:132px;top:1px">Document</span><span style="left:197px;top:1px">Description</span></div>
    <div class="photo" style="left:104px;top:162px;width:18px;height:22px" role="img" aria-label="Product package photo"></div>
    <div class="abs" style="left:132px;top:180px;text-decoration:underline">gummy_bag.jpeg</div>
    <div class="btn" style="left:243px;top:190px;width:27px;height:6px">Cancel</div>
    <div class="btn" style="left:275px;top:190px;width:27px;height:6px">Update</div>
    <div class="abs" style="left:0;top:198px;width:308px;font-size:3.2px"><span class="abs" style="left:0">Gumdrop - 90mg - 20</span><span class="abs" style="left:37px">8900134</span><span class="abs" style="left:65px">THC Infused Edibles</span><span class="abs" style="left:117px">06/15/15</span><span class="abs" style="left:153px">$32.95</span><span class="abs" style="left:169px">$28.95</span><span class="abs" style="left:222px">04/30/99</span></div>
  </div>

  <!-- Edit order screen -->
  <div class="screen" style="left:262px;top:530px;width:300px;height:220px">
    <div class="abs" style="left:18px;top:6px;font-size:5.5px;color:#333;font-weight:600">Edit Order</div>
    <div class="abs" style="left:9px;top:13px;width:6px;height:6px;border-radius:50%;background:var(--blue);color:#fff;font-size:3.6px;text-align:center;line-height:6px">2</div>
    <div class="abs" style="left:18px;top:14px;font-size:4.4px;color:var(--blue)">Select your desired products and quantities, then change status to Order Placed, and Submit</div>
    <div class="lbl" style="left:40px;top:27px;width:40px">Location:</div><div class="abs" style="left:82px;top:26px;font-size:3.8px;color:#333">Harbor Point Store</div>
    <div class="lbl" style="left:40px;top:37px;width:40px">Customer:</div><div class="abs" style="left:82px;top:36px;font-size:3.6px;color:#333">Bramblewood Dispensary</div>
    <div class="lbl" style="left:40px;top:47px;width:40px">Req. Delivery Date:</div><div class="field" style="left:82px;top:46px;width:20px">9/30/2019</div>
    <div class="lbl" style="left:40px;top:62px;width:40px">Order Notes:</div><div class="field" style="left:82px;top:55px;width:52px;height:15px">Please deliver after 1:00pm. Store manager must sign off on receipt</div>
    <div class="lbl" style="left:160px;top:27px;width:42px">New Status:</div><div class="field" style="left:157px;top:26px;width:52px;left:157px">Reviewed - Approved</div>
    <div class="lbl" style="left:160px;top:36px;width:42px">Status Reason:</div><div class="field" style="left:157px;top:35px;width:52px"></div>
    <div class="lbl" style="left:160px;top:46px;width:42px">PO Number:</div><div class="field" style="left:157px;top:45px;width:52px">2019-124A</div>
    <div class="lbl" style="left:160px;top:56px;width:42px">Create Date:</div><div class="abs" style="left:157px;top:56px;font-size:3.4px">September 13, 2019</div>
    <div class="lbl" style="left:160px;top:66px;width:42px">Order Total:</div><div class="abs" style="left:157px;top:66px;font-size:3.4px">$19,465.00</div>
    <div class="abs" style="left:218px;top:25px;width:72px;height:22px;border:.5px solid #ccc;padding:2px 3px;font-size:3px">Reviewed - Approved
      <svg width="66" height="7" style="display:block;margin-top:1px"><rect x="0" y="0" width="66" height="7" rx="3.5" fill="#e3e3e3"/><rect x="0" y="0" width="20" height="7" rx="3.5" fill="var(--green)"/></svg>Next Step: Invoicing</div>
    <div class="btn" style="left:267px;top:58px;width:25px;height:6px">Submit</div>
    <div class="abs" style="left:20px;top:80px;width:270px;border-bottom:.5px solid #ddd;height:8px;font-size:3.4px;color:var(--blue);word-spacing:5px">Order Notes Customer Location Activity Contacts Invoices Documents Sales&nbsp;Management Instructions</div>
    <div class="abs" style="left:20px;top:90px;width:260px;height:130px;background:var(--panel)"></div>
    <div class="abs" style="left:22px;top:92px;font-style:italic;font-size:3.2px">Product Ordering Details</div>
    <div class="lbl" style="left:40px;top:101px;width:42px">Shipping &amp; Handling:</div>
    <div class="lbl" style="left:40px;top:109px;width:42px">Tax:</div>
    <div class="lbl" style="left:40px;top:117px;width:42px">Shipper:</div><div class="field" style="left:85px;top:116px;width:45px">Choose One</div>
    <div class="lbl" style="left:40px;top:125px;width:42px">Tracking Number:</div><div class="field" style="left:85px;top:124px;width:45px"></div>
    <div class="abs" style="left:24px;top:135px;font-size:3.2px">Ordered Products</div>
    <div class="abs" style="left:160px;top:135px;font-size:3.2px">Product Total: $19,465.00</div>
    <div class="btn" style="left:207px;top:133px;width:32px;height:6px;font-size:3.2px">Generate Invoice</div>
    <div class="btn" style="left:241px;top:133px;width:40px;height:6px;font-size:3.2px">Send To LedgerBook</div>
    <div class="abs" style="left:22px;top:145px;width:256px;height:75px;background:#fff;border:.5px solid #ddd">
      <div class="row" style="top:0;height:10px"><span style="left:25px;top:3px">Product</span><span style="left:150px;top:3px">Price</span><span style="left:192px;top:3px">Quantity</span><span style="left:229px;top:3px">Total</span></div>
      <div class="photo" style="left:5px;top:12px;width:6px;height:18px;background:linear-gradient(#7a6aa0,#c9b9e0)" role="img" aria-label="Dropper bottle product photo"></div>
      <div class="row" style="top:10px;height:32px"><span style="left:25px;top:22px">780090: CBD Oil: CBD Drops - 1000mg 1oz</span><span style="left:150px;top:22px">$17.95</span><span style="left:192px;top:21px">300</span><span style="left:229px;top:21px">$5,385.00</span></div>
      <div class="photo" style="left:5px;top:47px;width:10px;height:12px;background:linear-gradient(#c0504d,#e9a3a1)" role="img" aria-label="Gummy pack product photo"></div>
      <div class="row" style="top:42px;height:33px;border:0"><span style="left:25px;top:22px">8901134: THC Infused Edibles: Gumdrop THC - 90 mg</span><span style="left:150px;top:22px">$28.95 on sale</span><span style="left:192px;top:20px">400</span><span style="left:229px;top:20px">$11,580.00</span></div>
    </div>
  </div>

  <!-- Right page -->
  <div class="block" style="left:642px;top:34px;width:535px">
    <h2>Compliance and Tracking</h2>
    <p style="margin-top:4px">Comply with state regulations by keeping track of retailer licenses and expiration dates. The license number for each retailer is stored and shown on invoicing. Sales are tracked by retailer and location, providing a quick view of sales history and export for off-line reporting when needed.<br>Upload your CoAs to your sales portal to provide retailers the ability to quickly and easily download at any time.</p>
  </div>
  <div class="block" style="left:642px;top:154px;width:215px">
    <h2>Grow Your Retail Sales</h2>
    <h3 style="margin-top:6px">Manage Retailer Leads to Expand Your Channel</h3>
    <p style="margin-top:8px">Your business development team can track and manage retailer leads to expand your sales channel. They can enter leads manually or upload them from external lists. When a retailer agrees to join your sales channel, set them up as authorized retailers and they are ready to place orders.</p>
  </div>
  <div class="block" style="left:642px;top:338px;width:535px">
    <h3>Manage On-site Marketing Activities</h3>
    <p style="margin-top:6px">Frequent on-site brand development activities at retailer locations help increase sell-through rates. Our software provides tools to coordinate those activities with your sales managers. Use the system to manage lunch-and-learns, training, sampling and other promotions.</p>
    <h3 style="margin-top:13px">Use Co-Marketing Funds to Increase Retailer Sales</h3>
    <p style="margin-top:6px">Provide retailers with funding for cooperative marketing campaigns. Successful campaigns can yield returns as high as 3,000% but managing this kind of program is an administrative challenge. Our software helps manage all aspects of a Co-marketing campaign – from retailer contract management through payment with performance metrics reporting throughout.</p>
  </div>

  <!-- Customer dashboard -->
  <div class="screen" style="left:868px;top:155px;width:307px;height:167px">
    <div class="abs" style="left:1px;top:3px;font-size:4.2px;color:#333">Customer Dashboard</div>
    <div class="abs" style="left:2px;top:14px;width:300px;border-bottom:.5px solid #ddd;height:7px;color:var(--blue);font-size:3px;word-spacing:8px">Customers Groups Add&nbsp;Customer Usage</div>
    <div class="field" style="left:2px;top:24px;width:26px"></div><div class="btn" style="left:29px;top:24px;width:18px;height:6px;font-size:3px">Find</div>
    <div class="abs" style="left:51px;top:25px;font-size:3px">Customer Status:</div><div class="field" style="left:72px;top:24px;width:34px">Active Customers</div>
    <div class="abs thead" style="left:2px;top:33px;width:304px;height:9px;font-size:3px"><span style="left:1px;top:1px">Customer</span><span style="left:60px;top:1px">Customer ID</span><span style="left:106px;top:1px">Country</span><span style="left:129px;top:1px">Characteristics</span><span style="left:178px;top:1px">Tax ID</span><span style="left:192px;top:1px">Customer Type</span><span style="left:258px;top:1px">Groups Users Active</span></div>
    <div class="abs" style="left:2px;top:42px;width:304px;height:45px;font-size:3px">
      <div class="row" style="top:0;height:6px"><span style="left:1px;color:var(--blue)">Fern Hollow</span><span style="left:106px">United States</span><span style="left:192px">Retailer</span></div>
      <div class="row" style="top:6px;height:6px"><span style="left:1px;color:var(--blue)">Moss Co.</span><span style="left:106px">United States</span><span style="left:192px">Retailer</span></div>
      <div class="row" style="top:12px;height:6px"><span style="left:1px;color:var(--blue)">Oak Shop</span><span style="left:106px">United States</span><span style="left:192px">Retailer</span></div>
      <div class="row" style="top:18px;height:6px"><span style="left:1px;color:var(--blue)">Sage Acre</span><span style="left:106px">United States</span><span style="left:192px">Distributor</span></div>
      <div class="row" style="top:24px;height:6px;background:#f4f4f4"><span style="left:1px;color:var(--blue)">Bramblewood Dispensary</span><span style="left:106px">United States</span><span style="left:192px">Retailer</span></div>
    </div>
    <div class="abs" style="left:2px;top:72px;width:304px;height:88px;background:#fafafa"></div>
    <div class="lbl" style="left:40px;top:80px;width:36px">Customer Name:</div><div class="abs" style="left:80px;top:80px;font-size:3px;color:#333">Bramblewood Dispensary</div>
    <div class="lbl" style="left:40px;top:90px;width:36px">Customer ID:</div><div class="field" style="left:80px;top:89px;width:30px">2019-21</div>
    <div class="lbl" style="left:40px;top:98px;width:36px">eMail Domain:</div><div class="field" style="left:80px;top:97px;width:48px">bramble.com</div>
    <div class="lbl" style="left:40px;top:106px;width:36px">Sales Manager:</div><div class="field" style="left:80px;top:105px;width:48px">Lia Moss (lia@fernway.com)</div>
    <div class="lbl" style="left:180px;top:80px;width:26px">Country:</div><div class="field" style="left:210px;top:79px;width:36px">United States</div>
    <div class="lbl" style="left:180px;top:89px;width:26px">Customer Type:</div><div class="field" style="left:210px;top:88px;width:36px">Retailer</div>
    <div class="lbl" style="left:180px;top:98px;width:26px">License #:</div><div class="field" style="left:210px;top:97px;width:36px">2019-Rec</div>
    <div class="lbl" style="left:180px;top:107px;width:26px">State:</div><div class="field" style="left:210px;top:106px;width:36px">California</div>
    <div class="lbl" style="left:180px;top:116px;width:26px">Date:</div><div class="field" style="left:210px;top:115px;width:30px">4/4/2019</div>
    <div class="lbl" style="left:180px;top:124px;width:26px">License #:</div><div class="field" style="left:210px;top:123px;width:36px">2019-Med</div>
    <div class="lbl" style="left:180px;top:132px;width:26px">State:</div><div class="field" style="left:210px;top:131px;width:36px">California</div>
    <div class="btn" style="left:255px;top:140px;width:15px;height:5px;font-size:2.8px">Update</div><div class="btn" style="left:272px;top:140px;width:15px;height:5px;font-size:2.8px">Cancel</div>
    <div class="abs" style="left:2px;top:149px;width:304px;height:18px;font-size:3px">
      <div class="row" style="top:0;height:6px"><span style="left:1px;color:var(--blue)">Ridgeview Dispensary</span><span style="left:106px">United States</span><span style="left:192px">Retailer</span></div>
      <div class="row" style="top:6px;height:6px"><span style="left:1px;color:var(--blue)">Pine Valley</span><span style="left:106px">United States</span><span style="left:192px">Retailer</span></div>
      <div class="row" style="top:12px;height:6px"><span style="left:1px;color:var(--blue)">Cedar Post</span><span style="left:106px">United States</span><span style="left:192px">Retailer</span></div>
    </div>
  </div>

  <!-- Performance screen -->
  <div class="screen" style="left:700px;top:505px;width:422px;height:245px;font-size:4px">
    <div class="abs" style="left:1px;top:2px;font-size:7.5px;color:#333;font-family:'Quicksand',sans-serif;font-weight:600">Performance</div>
    <div class="abs" style="left:0;top:14px;width:422px;height:70px;background:var(--panel)"></div>
    <div class="abs" style="left:4px;top:16px;font-size:7px;color:#888">Performance Snapshot</div>
    <div class="abs" style="right:8px;top:22px;font-size:3.8px">As of: 9/13/19</div>
    <div class="abs" style="left:44px;top:38px;font-size:3.8px;line-height:6px;text-align:right">Pipeline Value:<br>Closed Value:<br>Weighted Value:</div>
    <div class="abs" style="left:78px;top:38px;font-size:3.8px;line-height:6px">$82,019<br>$3,805<br>$16,102</div>
    <div class="abs" style="left:176px;top:47px;font-size:3.8px;line-height:6px;text-align:right">Average Sales Stage: 60%<br>Close Ratio: 5:19</div>
    <div class="abs" style="left:302px;top:30px;width:112px;height:38px;background:#fff;border:.5px solid #dde">
      <svg width="112" height="38">
        <line x1="12" y1="4" x2="12" y2="28" stroke="#555" stroke-width=".5"/><line x1="12" y1="28" x2="60" y2="28" stroke="#555" stroke-width=".5"/>
        <rect x="14" y="12" width="3" height="16" fill="#f0a030"/><rect x="18" y="6" width="3" height="22" fill="#d9e021"/>
        <rect x="28" y="16" width="3" height="12" fill="#f0a030"/><rect x="32" y="8" width="3" height="20" fill="#d9e021"/>
        <rect x="42" y="10" width="3" height="18" fill="#f0a030"/><rect x="46" y="12" width="3" height="16" fill="#d9e021"/>
        <text x="13" y="34" font-size="3.6" fill="#333">Pipeline   Closed   Payments</text>
        <rect x="68" y="13" width="4" height="1" fill="#f0a030"/><text x="74" y="14.5" font-size="3.4" fill="#333">Avg</text>
        <rect x="68" y="18" width="4" height="1" fill="#d9e021"/><text x="74" y="19.5" font-size="3.4" fill="#333">My Customers</text>
      </svg>
    </div>
    <div class="abs" style="left:2px;top:84px;width:3px;height:3px;border:.5px solid #999"></div>
    <div class="abs" style="left:8px;top:83px;font-size:3.6px">Show only my customers</div>
    <div class="abs" style="left:96px;top:85px;font-size:3.8px">Customer:</div><div class="field" style="left:117px;top:83px;width:70px;height:8px;line-height:7px;font-size:3.6px">Ridgeview Dispensary</div>
    <div class="abs" style="left:14px;top:95px;width:300px;height:17px;background:var(--panel)"></div>
    <div class="abs" style="left:16px;top:100px;font-size:3.6px">Items Per Page:</div><div class="field" style="left:45px;top:99px;width:8px;height:7px">12</div>
    <div class="abs" style="left:60px;top:101px;font-size:3.6px">Start Date:</div><div class="field" style="left:80px;top:99px;width:24px;height:7px">1/1/2009</div>
    <div class="abs" style="left:165px;top:101px;font-size:3.6px">End Date:</div><div class="field" style="left:183px;top:99px;width:24px;height:7px">9/13/2019</div>
    <div class="abs" style="left:1px;top:122px;font-size:7.5px;color:#333;font-family:'Quicksand',sans-serif;font-weight:600">Orders</div>
    <div class="abs thead" style="left:2px;top:135px;width:420px;height:7px;font-size:3.8px"><span style="left:2px;top:1px">Customer</span><span style="left:108px;top:1px">Location</span><span style="left:200px;top:1px">Order Date</span><span style="left:258px;top:1px">Status</span><span style="left:338px;top:1px">Percent Complete</span></div>
    <div class="abs" style="left:2px;top:142px;width:420px;height:103px;font-size:3.6px;color:#888">
      <div class="row" style="top:0;height:8.4px"><span style="left:2px;top:2px">Ridgeview Dispensary</span><span style="left:108px;top:2px">Dell's Apothecary</span><span style="left:200px;top:2px">5/31/19</span><span style="left:258px;top:2px">Delivery Date Set</span><span style="left:338px;top:2px">87%</span></div>
      <div class="row" style="top:8.4px;height:8.4px"><span style="left:2px;top:2px">Ridgeview Dispensary</span><span style="left:108px;top:2px">Tiny Leaf Dispensary</span><span style="left:200px;top:2px">5/7/19</span><span style="left:258px;top:2px">Invoice Sent</span><span style="left:338px;top:2px">50%</span></div>
      <div class="row" style="top:16.8px;height:8.4px"><span style="left:2px;top:2px">Ridgeview Dispensary</span><span style="left:108px;top:2px">Tiny Leaf Dispensary</span><span style="left:200px;top:2px">5/7/19</span><span style="left:258px;top:2px">Order Placed</span><span style="left:338px;top:2px">12%</span></div>
      <div class="row" style="top:25.2px;height:8.4px"><span style="left:2px;top:2px">Ridgeview Dispensary</span><span style="left:108px;top:2px">Dell's Apothecary</span><span style="left:200px;top:2px">5/7/19</span><span style="left:258px;top:2px">Invoice Sent</span><span style="left:338px;top:2px">50%</span></div>
      <div class="row" style="top:33.6px;height:8.4px"><span style="left:2px;top:2px">Ridgeview Dispensary</span><span style="left:108px;top:2px">Harbor Point Store</span><span style="left:200px;top:2px">5/7/19</span><span style="left:258px;top:2px">Invoice Sent</span><span style="left:338px;top:2px">50%</span></div>
      <div class="row" style="top:42px;height:8.4px"><span style="left:2px;top:2px">Ridgeview Dispensary</span><span style="left:108px;top:2px">Harbor Point Store</span><span style="left:200px;top:2px">5/7/19</span><span style="left:258px;top:2px">Payment Received</span><span style="left:338px;top:2px">75%</span></div>
      <div class="row" style="top:50.4px;height:8.4px"><span style="left:2px;top:2px">Ridgeview Dispensary</span><span style="left:108px;top:2px">Harbor Point Store</span><span style="left:200px;top:2px">5/7/19</span><span style="left:258px;top:2px">Invoice Sent</span><span style="left:338px;top:2px">50%</span></div>
      <div class="row" style="top:58.8px;height:8.4px"><span style="left:2px;top:2px">Ridgeview Dispensary</span><span style="left:108px;top:2px">Dell's Apothecary</span><span style="left:200px;top:2px">5/7/19</span><span style="left:258px;top:2px">Order Placed</span><span style="left:338px;top:2px">12%</span></div>
      <div class="row" style="top:67.2px;height:8.4px"><span style="left:2px;top:2px">Ridgeview Dispensary</span><span style="left:108px;top:2px">Harbor Point Store</span><span style="left:200px;top:2px">5/3/19</span><span style="left:258px;top:2px">Order in Process</span><span style="left:338px;top:2px">62%</span></div>
      <div class="row" style="top:75.6px;height:8.4px"><span style="left:2px;top:2px">Ridgeview Dispensary</span><span style="left:108px;top:2px">Harbor Point Store</span><span style="left:200px;top:2px">5/1/19</span><span style="left:258px;top:2px">Order Placed</span><span style="left:338px;top:2px">12%</span></div>
      <div class="row" style="top:84px;height:8.4px"><span style="left:2px;top:2px">Ridgeview Dispensary</span><span style="left:108px;top:2px">Harbor Point Store</span><span style="left:200px;top:2px">4/25/19</span><span style="left:258px;top:2px">Order Shipped</span><span style="left:338px;top:2px">100%</span></div>
      <div class="row" style="top:92.4px;height:8.4px"><span style="left:2px;top:2px">Ridgeview Dispensary</span><span style="left:108px;top:2px">Harbor Point Store</span><span style="left:200px;top:2px">4/24/19</span><span style="left:258px;top:2px">Order Shipped</span><span style="left:338px;top:2px">100%</span></div>
    </div>
  </div>
</div>
</body>
</html>
```